New Business Card Design Project

I'd like a business card design around the same modern style that I used on my website www.brisklyms.net
It's gonna be one of those round corners double-sided business cards with maybe a big logo on the front and all the info on the back of the card.

Contact Information for Business Card

Marco Deltoro
425-736-5184
www.brisklyms.net

www.facebook.com/BrisklyMaidServices
www.intsgram.com/BrisklyMaidServices

Requirements
Must have
• it needs to look elegant and modern

```html
<!DOCTYPE html>
<html lang="en">
<head>
<meta charset="utf-8">
<title>Briskly Maid Services – Business Card</title>
<link rel="stylesheet" href="https://fonts.googleapis.com/css2?family=Work+Sans:wght@400;500;600&display=swap">
<style>
  :root {
    --page-bg: #e6e8eb;
    --card-white: #ffffff;
    --card-dark: #262629;
    --brand-blue: #1b8ed8;
    --text-dark: #2a2a2e;
  }
  * { box-sizing: border-box; margin: 0; padding: 0; }
  html, body {
    width: 1200px; height: 900px; overflow: hidden;
    background: var(--page-bg);
    font-family: "Work Sans", Arial, sans-serif;
  }
  .card {
    position: absolute;
    left: 280px;
    width: 640px; height: 366px;
    border-radius: 18px;
    box-shadow: 0 10px 30px rgba(0,0,0,.18);
    overflow: hidden;
  }
  .card--front { top: 54px; background: var(--card-white); }
  .card--back { top: 480px; background: var(--card-dark); }

  .brand-name {
    position: absolute; left: 40px; top: 34px;
    display: flex; align-items: center; gap: 10px;
    color: var(--brand-blue); font-weight: 600; font-size: 30px; letter-spacing: .5px;
  }
  .brand-dot { width: 14px; height: 14px; border-radius: 50%; background: var(--brand-blue); }

  .person { position: absolute; right: 62px; top: 100px; text-align: right; }
  .person-name {
    color: var(--brand-blue); font-size: 30px; font-weight: 500; letter-spacing: 1.5px;
    text-transform: uppercase; line-height: 1;
  }
  .person-title { margin-top: 8px; color: var(--text-dark); font-size: 17px; line-height: 20px; }

  .divider {
    position: absolute; left: 36px; right: 60px; top: 170px;
    height: 2px; background: var(--brand-blue);
  }

  .contact-list {
    position: absolute; left: 36px; top: 196px; list-style: none;
    color: var(--text-dark); font-size: 15px; line-height: 24px;
  }
  .contact-list li { display: flex; align-items: center; gap: 10px; }
  .contact-icon { width: 13px; height: 13px; flex: none; }

  .address {
    position: absolute; right: 62px; bottom: 36px; text-align: right;
    color: var(--text-dark); font-size: 16px; line-height: 24px;
  }

  .back-brand {
    position: absolute; inset: 0;
    display: flex; align-items: center; justify-content: center; gap: 16px;
    color: var(--brand-blue); font-weight: 600; font-size: 46px; letter-spacing: 1px;
  }
  .back-brand .brand-dot { width: 22px; height: 22px; }
</style>
</head>
<body>
  <section class="card card--front" aria-label="Business card, information side">
    <div class="brand-name"><span class="brand-dot"></span>Briskly Maid Services</div>
    <div class="person">
      <p class="person-name">Marco Deltoro</p>
      <p class="person-title">Director</p>
    </div>
    <div class="divider"></div>
    <ul class="contact-list">
      <li>
        <svg class="contact-icon" viewBox="0 0 16 16" fill="#1b8ed8"><path d="M4 1l3 3-2 2c1 2 3 4 5 5l2-2 3 3-2 3C7 15 1 9 1 3z"/></svg>
        425-736-5184
      </li>
      <li>
        <svg class="contact-icon" viewBox="0 0 16 16" fill="none" stroke="#1b8ed8" stroke-width="1.6"><rect x="1" y="3" width="14" height="10"/><path d="M1 3l7 6 7-6"/></svg>
        info@brisklyms.net
      </li>
      <li>
        <svg class="contact-icon" viewBox="0 0 16 16" fill="none" stroke="#1b8ed8" stroke-width="1.4"><circle cx="8" cy="8" r="6.5"/><ellipse cx="8" cy="8" rx="3" ry="6.5"/><path d="M1.5 8h13"/></svg>
        www.brisklyms.net
      </li>
      <li>
        <svg class="contact-icon" viewBox="0 0 16 16"><circle cx="8" cy="8" r="6" fill="#1b8ed8"/></svg>
        /BrisklyMaidServices
      </li>
      <li>
        <svg class="contact-icon" viewBox="0 0 16 16"><rect x="2" y="2" width="12" height="12" fill="#1b8ed8"/></svg>
        /BrisklyMaidServices
      </li>
    </ul>
    <p class="address">2740 Alder Creek Road<br>Oklahoma City, OK 73010</p>
  </section>

  <section class="card card--back" aria-label="Business card, brand side">
    <div class="back-brand"><span class="brand-dot"></span>Briskly Maid Services</div>
  </section>
</body>
</html>
```